Torvik pressure washing environmental truck Wrap design

Need a custom wrap for my pressure washing custom truck. Design must look environmental, and clean. Website is
PineHollowHygiene.com
Tag line ; " Trash Can / Dumpster Sanitation.... Pressure Washing & Soft Washing Experts "
Ive attached some current designs for the truck that i wasnt satisfied with..
Design should be clean, easy to read, environmental, etc.

Target Market(s)

Home owners, business owners, property managers

Colors

Designer to choose colors to be used in the design.

Requirements
Nice to have
• One of the designers used a photo which i really like the concept but i would lile the photo to be of someone pressure washing a building or house instead. I uploaded the design. And change the purple to blue or green

```html
<!DOCTYPE html>
<html lang="en">
<head>
<meta charset="utf-8">
<title>Torvik Truck Wrap</title>
<link href="https://fonts.googleapis.com/css2?family=Poppins:wght@500;600;700;800&display=swap" rel="stylesheet">
<style>
  :root{
    --green:#3aaa48;
    --blue:#1f6fb8;
    --blue-bright:#1e88d8;
    --white:#ffffff;
    --ink:#3a3a3a;
    --badge-dark:#1f3d1f;
    --badge-red:#b8322e;
  }
  *{margin:0;padding:0;box-sizing:border-box;}
  html,body{width:1200px;height:1200px;overflow:hidden;background:var(--white);}
  body{font-family:"Poppins",sans-serif;position:relative;}
  .wrap-panel{position:absolute;left:40px;top:430px;width:1120px;height:340px;}
  .wrap-panel svg.panel-shapes{position:absolute;inset:0;}
  .headline{position:absolute;left:0;width:612px;text-align:center;color:var(--white);font-weight:600;}
  .headline--services{top:10px;font-size:27px;}
  .headline--claim{top:50px;font-size:24px;font-weight:500;}
  .headline--claim b{color:var(--blue-bright);font-weight:700;}
  .brand{position:absolute;left:14px;top:112px;width:600px;text-align:center;}
  .brand-name{font-size:38px;font-weight:700;letter-spacing:0.5px;line-height:1;}
  .brand-name .pine{color:var(--green);}
  .brand-name .hygiene{color:var(--blue);}
  .brand-dot{font-size:14px;color:var(--blue);font-weight:700;writing-mode:vertical-rl;vertical-align:top;margin-left:2px;}
  .brand-services{display:flex;align-items:center;justify-content:center;gap:12px;margin-top:6px;
    font-size:27px;font-weight:600;letter-spacing:9px;color:var(--ink);line-height:1;}
  .brand-services::before,.brand-services::after{content:"";display:block;width:150px;height:2px;background:var(--ink);}
  .brand-tag{margin-top:6px;font-size:17px;font-weight:500;letter-spacing:5px;color:var(--ink);}
  .phone{position:absolute;left:0;top:242px;width:612px;text-align:center;color:var(--white);
    font-size:60px;font-weight:700;letter-spacing:1px;}
  .seal-name{position:absolute;left:656px;top:140px;width:280px;text-align:center;
    font-size:46px;font-weight:700;color:var(--blue);letter-spacing:2px;}
</style>
</head>
<body>
  <div class="wrap-panel">
    <svg class="panel-shapes" width="1120" height="340" viewBox="0 0 1120 340">
      <rect x="0" y="0" width="940" height="98" fill="var(--green)"/>
      <polygon points="940,0 1040,0 1120,70 1120,182 940,182" fill="var(--white)"/>
      <rect x="0" y="98" width="1120" height="7" fill="var(--blue)"/>
      <rect x="0" y="105" width="1120" height="4" fill="var(--green)"/>
      <rect x="0" y="109" width="940" height="121" fill="var(--white)"/>
      <rect x="0" y="230" width="940" height="5" fill="var(--blue)"/>
      <rect x="0" y="240" width="940" height="98" fill="var(--blue)"/>
      <circle cx="796" cy="166" r="138" fill="var(--white)" stroke="var(--blue)" stroke-width="12"/>
      <path d="M965 30 h70 v30 q0 20 -35 34 q-35 -14 -35 -34 z" fill="var(--badge-red)"/>
      <rect x="958" y="122" width="98" height="46" rx="4" fill="var(--badge-dark)"/>
    </svg>

    <p class="headline headline--services">Commercial Residential</p>
    <p class="headline headline--claim">Kills <b>99,9%</b> Off All <b>GERM</b> and <b>BACTERIA</b></p>

    <div class="brand">
      <p class="brand-name"><span class="pine">PINE HOLLOW</span> <span class="hygiene">HYGIENE</span><span class="brand-dot">.com</span></p>
      <p class="brand-services">SERVICES</p>
      <p class="brand-tag">TRASH BINS AND MORE</p>
    </div>

    <p class="phone">123-456-7890</p>

    <p class="seal-name">TORVIK</p>
  </div>
</body>
</html>
```